Singapore Restaurant Menu Design

We need a menu designed for our new Singapore inspire restaurant located here in New Plymouth New Zealand. More Information in attached documents.
Updates

Sick

Target Market(s)

New Zealanders

Colors

Designer to choose only greyscale colors for use in the design.

Requirements
Nice to have
• Images of Singapore food however we do not want this to distract from the overall menu design as we still want the menu to be super clean

```html
<!DOCTYPE html>
<html lang="en">
<head>
<meta charset="utf-8">
<title>Menu – Roti &amp; Noodles</title>
<link href="https://fonts.googleapis.com/css2?family=Arimo:ital,wght@0,400;0,700;1,400&display=swap" rel="stylesheet">
<style>
  :root {
    --frame: #d9d9d9;
    --paper-light: #f7f7f7;
    --paper-mid: #ececec;
    --paper-dark: #d6d6d6;
    --ink: #222222;
    --ornament: #c4c4c4;
  }
  * { box-sizing: border-box; margin: 0; padding: 0; }
  html, body { width: 849px; height: 1200px; overflow: hidden; }
  body { font-family: "Arimo", Arial, sans-serif; color: var(--ink); }

  .menu-page {
    position: relative;
    width: 849px;
    height: 1200px;
    border: 8px solid var(--frame);
    background:
      radial-gradient(ellipse 60% 55% at 40% 40%, var(--paper-light) 0%, rgba(247,247,247,0) 70%),
      linear-gradient(100deg, var(--paper-mid) 0%, var(--paper-light) 35%, var(--paper-light) 62%, var(--paper-dark) 100%);
    overflow: hidden;
  }

  .flourish { position: absolute; opacity: 0.5; }
  .flourish--right {
    right: 0; top: 640px; width: 150px; height: 560px;
    background: radial-gradient(ellipse 70% 60% at 100% 65%, var(--ornament) 0%, rgba(196,196,196,0) 100%);
  }
  .flourish--bottom-left {
    left: 0; bottom: 0; width: 240px; height: 170px;
    background: radial-gradient(ellipse at 30% 80%, rgba(255,255,255,0.8) 0%, rgba(255,255,255,0) 70%);
  }

  .dish { position: absolute; left: 100px; width: 618px; }

  .dish__head {
    display: flex;
    align-items: baseline;
    white-space: nowrap;
  }
  .dish__name { font-weight: 700; font-size: 25.5px; }
  .dish__leader {
    flex: 1;
    overflow: hidden;
    font-weight: 700;
    font-size: 19px;
    letter-spacing: 4.2px;
    padding: 0 6px 0 8px;
    text-align: right;
    direction: rtl;
  }
  .dish__price { font-weight: 700; font-size: 19px; }

  .dish__desc {
    font-style: italic;
    font-size: 19px;
    letter-spacing: 0.3px;
    line-height: 24.5px;
    text-align: justify;
    text-align-last: left;
  }

  .section-title {
    position: absolute;
    left: 0; right: 0; top: 364px;
    text-align: center;
    font-weight: 700;
    font-size: 31px;
    text-decoration: underline;
    text-decoration-thickness: 2px;
    text-underline-offset: 4px;
  }
</style>
</head>
<body>
<main class="menu-page">
  <div class="flourish flourish--right" role="img" aria-label="Faint grey floral flourish along the right edge"></div>
  <div class="flourish flourish--bottom-left" role="img" aria-label="Faint pale floral flourish in the lower left corner"></div>

  <section class="dish" style="top:81px">
    <div class="dish__head"><span class="dish__name">Roti Jala - Malay netted crepe</span><span class="dish__leader">. . . . . . . . . . . . . . . . . . . . . . . . . . . . . .</span><span class="dish__price">$15.00</span></div>
    <p class="dish__desc" style="margin-top:20px">Flour &amp; egg based batter spiced with tumeric and cumin accompanied with choice of chicken or veg curry.</p>
  </section>

  <section class="dish" style="top:223px">
    <div class="dish__head"><span class="dish__name">Murtabak - stuffed prata</span><span class="dish__leader">. . . . . . . . . . . . . . . . . . . . . . . . . . . . . . . . . . . .</span><span class="dish__price">$15.00</span></div>
    <p class="dish__desc" style="margin-top:4px">Flour based crispy flat bread stuffed with choice of double cooked chicken curry, sauteed beef or seasonal veg curry.</p>
  </section>

  <h2 class="section-title">Noodles</h2>

  <section class="dish" style="top:459px">
    <div class="dish__head"><span class="dish__name">Wonton noodles</span><span class="dish__leader">. . . . . . . . . . . . . . . . . . . . . . . . . . . . . . . . . . . . . . . . . . . . . . . . . . . . . . . . .</span><span class="dish__price">$15.00</span></div>
    <p class="dish__desc" style="margin-top:24px">Wonton noodles tossed in sweet dark soy sauce, sesame oil topped with pickled chili, cucumber &amp; broth with choice of bbq pork, chicken or prawns and fried crispy wontons.</p>
  </section>

  <section class="dish" style="top:623px">
    <div class="dish__head"><span class="dish__name">Seafood mee goreng</span><span class="dish__leader">. . . . . . . . . . . . . . . . . . . . . . . . . . . . . . . . . . . . . . . .</span><span class="dish__price">$18.00</span></div>
    <p class="dish__desc" style="margin-top:21px">Wok fried Malay style egg noodles in a homemade chili paste with prawns and squid topped with fried egg.</p>
  </section>

  <section class="dish" style="top:765px">
    <div class="dish__head"><span class="dish__name">Veggie mee goreng V</span><span class="dish__leader">. . . . . . . . . . . . . . . . . . . . . . . . . . . . . . . . . . . . . . . .</span><span class="dish__price">$15.00</span></div>
    <p class="dish__desc" style="margin-top:20px">Wok fried Malay style egg noodles in homemade chili paste with seasonal veggies &amp; tofu.</p>
  </section>

  <section class="dish" style="top:907px">
    <div class="dish__head"><span class="dish__name">Char Kway Teow</span><span class="dish__leader">. . . . . . . . . . . . . . . . . . . . . . . . . . . . . . . . . . . . . . . . . . .</span><span class="dish__price">$15.00</span></div>
    <p class="dish__desc" style="margin-top:20px">Wok fried rice cake strips in sweet dark soy sauce, fish oil, chili paste with seafood topped with beansprouts.</p>
  </section>
</main>
</body>
</html>
```